To revamp the exting web page and Company presentation to new propsective client

We are company establish in 2006. We have a combine of Veltra implementation team of more than 10 years. We focus on the following areas

a) Veltra Nimbus suite implementation
b) Veltra Nimbus suite platform migration
c) Large database size in excess of 20TB

We need to redesign a our existing new card to give a new look and refresh look. Kindly visit our website for more info www.halvtek.com

Your main them is blue color and hope to hear from you all.

Target Market(s)

Professional clients

Industry/Entity Type

Information Technology

Contact Information for Business Card

To market our as the leading Veltra partner in Veltra nimbus suite implementation

Number of Pages Required

1 page

Colors
3276b5
9bcb3c
cadf82
33a6d7

Requirements
Must have
• The ability to attract new customer and show a level of professionalism.
• You can also add a green color to represent green and environmental friendly.
Nice to have
• To give a total new fresh look for the company
Should not have
• None

```html
<!DOCTYPE html>
<html lang="en">
<head>
<meta charset="utf-8">
<title>Halvtek Business Card</title>
<link href="https://fonts.googleapis.com/css2?family=Roboto:wght@400;500;700&display=swap" rel="stylesheet">
<style>
  :root {
    --backdrop: #2a2a2c;
    --cyan-light: #12c6d9;
    --cyan-deep: #0a8fb0;
    --navy: #1f2a5c;
    --accent-blue: #2a9fc9;
    --paper: #f4f4f2;
    --ink-grey: #555a60;
    --badge-red: #e41e26;
    --white: #ffffff;
  }
  * { margin: 0; padding: 0; box-sizing: border-box; }
  html, body { width: 1200px; height: 900px; overflow: hidden; }
  body {
    background: var(--backdrop);
    font-family: "Roboto", Arial, sans-serif;
    position: relative;
  }
  .card {
    position: absolute;
    width: 640px;
    height: 366px;
    box-shadow: 0 18px 40px rgba(0,0,0,.55);
  }
  .card-front {
    left: 70px; top: 70px;
    background: linear-gradient(135deg, var(--cyan-light) 0%, var(--cyan-deep) 100%);
    color: var(--white);
  }
  .card-back {
    left: 490px; top: 460px;
    background: var(--paper);
    color: var(--ink-grey);
  }
  .brand {
    position: absolute;
    display: flex;
    align-items: center;
    gap: 12px;
  }
  .brand-dot {
    width: 26px; height: 26px; border-radius: 50%;
    flex: none;
  }
  .brand-name {
    display: block;
    font-family: "Roboto", Arial, sans-serif;
    font-weight: 500;
    font-size: 40px;
    letter-spacing: 1px;
    line-height: 1;
  }
  .brand-tagline {
    display: block;
    font-family: "Roboto", Arial, sans-serif;
    font-weight: 400;
    font-size: 11px;
    letter-spacing: 1px;
    margin-top: 4px;
  }
  .card-front .brand { left: 90px; top: 128px; }
  .card-front .brand-dot { background: var(--white); }
  .card-front .brand-name { color: var(--white); }
  .card-front .brand-tagline { color: rgba(255,255,255,.85); }
  .services {
    position: absolute;
    left: 260px; top: 212px;
    font-size: 15px;
    line-height: 1.35;
    text-align: center;
    width: 220px;
  }
  .divider {
    position: absolute;
    left: 30px; right: 30px; top: 262px;
    height: 1px;
    background: rgba(255,255,255,.35);
  }
  .partner {
    position: absolute;
    left: 28px; bottom: 26px;
    display: flex; align-items: flex-start; gap: 8px;
  }
  .partner-badge {
    width: 96px; height: 30px;
    background: var(--badge-red);
  }
  .partner-label { font-size: 10px; font-weight: 700; line-height: 1.2; }
  .platform-badge {
    position: absolute;
    right: 40px; top: 30px;
    width: 30px; height: 30px; border-radius: 50%;
    background: var(--badge-red);
    border: 2px solid var(--white);
  }
  .card-back .brand { left: 200px; top: 44px; }
  .card-back .brand-dot { background: var(--navy); }
  .card-back .brand-name { color: var(--navy); }
  .card-back .brand-tagline { color: var(--accent-blue); }
  .address {
    position: absolute;
    right: 32px; top: 130px;
    text-align: right;
    font-size: 14px;
    font-style: normal;
    line-height: 1.45;
  }
  .address .web { font-weight: 700; letter-spacing: 2px; color: var(--ink-grey); }
  .person { position: absolute; left: 32px; top: 200px; }
  .person-name { font-size: 20px; font-weight: 700; color: var(--navy); }
  .person-role { font-size: 16px; color: var(--accent-blue); margin-bottom: 8px; }
  .contact-list { list-style: none; font-size: 13px; line-height: 1.5; }
  .contact-list li { display: flex; align-items: center; gap: 10px; }
  .contact-list svg { width: 12px; height: 12px; fill: var(--navy); flex: none; }
</style>
</head>
<body>

<section class="card card-front">
  <div class="platform-badge"></div>
  <div class="brand">
    <span class="brand-dot"></span>
    <div>
      <span class="brand-name">Halvtek</span>
      <span class="brand-tagline">Systems Sdn Bhd</span>
    </div>
  </div>
  <p class="services">Database • Nimbus Suite<br>Consulting • Support</p>
  <div class="divider"></div>
  <div class="partner">
    <span class="partner-badge"></span>
    <span class="partner-label">Gold<br>Partner</span>
  </div>
</section>

<section class="card card-back">
  <div class="brand">
    <span class="brand-dot"></span>
    <div>
      <span class="brand-name">Halvtek</span>
      <span class="brand-tagline">Systems Sdn Bhd</span>
    </div>
  </div>
  <address class="address">
    Suite 5.02, 5th Floor<br>
    Wisma Teralis<br>
    Jalan Cempaka Biru<br>
    50450 Kuala Lumpur, Malaysia<br>
    <span class="web">www.halvtek.com</span>
  </address>
  <div class="person">
    <p class="person-name">DANIEL KOH</p>
    <p class="person-role">Chief Operating Officer</p>
    <ul class="contact-list">
      <li><svg viewBox="0 0 12 12"><path d="M2 1h3l1 3-2 1a7 7 0 0 0 3 3l1-2 3 1v3a1 1 0 0 1-1 1A10 10 0 0 1 1 2a1 1 0 0 1 1-1z"/></svg>60 3 4118 7302</li>
      <li><svg viewBox="0 0 12 12"><path d="M2 1h3l1 3-2 1a7 7 0 0 0 3 3l1-2 3 1v3a1 1 0 0 1-1 1A10 10 0 0 1 1 2a1 1 0 0 1 1-1z"/></svg>65 6290 1457 (Singapore)</li>
      <li><svg viewBox="0 0 12 12"><rect x="1" y="5" width="10" height="6"/><rect x="3" y="1" width="6" height="3"/></svg>60 3 4118 7310</li>
      <li><svg viewBox="0 0 12 12"><path d="M3 0h6v12H3zM4 1v9h4V1z"/></svg>60 12 845 2261</li>
      <li><svg viewBox="0 0 12 12"><path d="M0 2h12v8H0zM1 3l5 4 5-4z"/></svg>danielkoh@halvtek.com</li>
    </ul>
  </div>
</section>

</body>
</html>
```